TR Advisory Business Cards - High End AV / Low Voltage Company

We are low voltage AV company that specializes in high end clients on the residential side and larger businesses on the commercial side. We want something modern, tech looking but also something that is extremely professional looking. We have uploaded our logos and postcards we already have in the field. Along with a picture of one of our wrapped vans. Our website is at www.trvadvisory.example and our primary colors are the orange, green, grey and blue all military color finishes.

We are interesting in the slogans "Pairing You with the Right Technology" or "Leading the Lowcountry in Tech"

Target Market(s)

We focus on 70% Commercial and 30% Residential Customers

Industry/Entity Type

Low Voltage, AV Company

Contact Information for Business Card

Name - Dorian Fairweather, Title - Owner, Office Phone - 555-714-3096, Mobile Phone - 555-802-4173, E-Mail - d@trvadvisory.example, Website: www.trvadvisory.example

Font styles to use
Sans Serif

Requirements
Must have
• Must have Name, Title, Work Phone & Mobile, Website and Logo.
Nice to have
• We want something that will impress our higher end clients with a great logo
Should not have
• Too traditional or plain.

```html
<!DOCTYPE html>
<html lang="en">
<head>
<meta charset="utf-8">
<title>TR Advisory — Business Cards</title>
<link rel="stylesheet" href="https://fonts.googleapis.com/css2?family=Arimo:wght@400;700&display=swap">
<style>
  :root {
    --backdrop: #3d3d3d;
    --brand-orange: #e96838;
    --card-white: #ffffff;
    --ink-light: #ffffff;
    --divider: rgba(255, 255, 255, 0.55);
  }
  * { box-sizing: border-box; margin: 0; padding: 0; }
  html, body {
    width: 1200px;
    height: 803px;
    overflow: hidden;
    background: var(--backdrop);
    font-family: "Arimo", Arial, sans-serif;
  }
  .sheet {
    position: relative;
    width: 1200px;
    height: 803px;
  }
  .card {
    position: absolute;
    top: 258px;
    width: 500px;
    height: 286px;
    border-radius: 22px;
  }
  .card--front {
    left: 70px;
    background: var(--brand-orange);
    color: var(--ink-light);
    display: flex;
    flex-direction: column;
    align-items: center;
    justify-content: center;
  }
  .card--back {
    left: 630px;
    background: var(--card-white);
    display: flex;
    align-items: center;
    justify-content: center;
  }
  .identity {
    display: flex;
    align-items: baseline;
    gap: 8px;
    margin-bottom: 14px;
    margin-left: 40px;
  }
  .identity__name {
    font-weight: 700;
    font-size: 21px;
    letter-spacing: 0.2px;
  }
  .identity__slash { font-size: 18px; }
  .identity__title { font-size: 12px; }
  .contacts {
    display: flex;
    align-items: stretch;
    gap: 14px;
  }
  .contacts__column {
    display: flex;
    flex-direction: column;
    gap: 5px;
    font-size: 12.5px;
  }
  .contacts__column--phones { align-items: flex-end; }
  .contacts__divider {
    width: 1px;
    background: var(--divider);
  }
  .contact-line {
    display: flex;
    align-items: center;
    gap: 6px;
    line-height: 15px;
  }
  .contact-line svg {
    width: 11px;
    height: 11px;
    flex: none;
  }
  .brand-name {
    font-weight: 700;
    font-size: 44px;
    color: var(--brand-orange);
    letter-spacing: 1px;
  }
</style>
</head>
<body>
<main class="sheet">
  <section class="card card--front" aria-label="Business card front">
    <div class="identity">
      <span class="identity__name">Dorian Fairweather</span>
      <span class="identity__slash">/</span>
      <span class="identity__title">Owner</span>
    </div>
    <div class="contacts">
      <div class="contacts__column contacts__column--phones">
        <div class="contact-line">
          <span>555-714-3096</span>
          <svg viewBox="0 0 12 12" aria-hidden="true"><path d="M2.5 1 L4.5 1 L5 3.5 L3.8 4.5 C4.5 6 6 7.5 7.5 8.2 L8.5 7 L11 7.5 L11 9.5 C11 10.5 10 11 9 11 C5 10.5 1.5 7 1 3 C1 2 1.5 1 2.5 1 Z" fill="currentColor"/></svg>
        </div>
        <div class="contact-line">
          <span>555-802-4173</span>
          <svg viewBox="0 0 12 12" aria-hidden="true"><rect x="3" y="0.8" width="6.5" height="10.4" rx="1" fill="none" stroke="currentColor" stroke-width="1.2"/><circle cx="6.25" cy="9.4" r="0.6" fill="currentColor"/></svg>
        </div>
      </div>
      <div class="contacts__divider"></div>
      <div class="contacts__column">
        <div class="contact-line">
          <svg viewBox="0 0 12 12" aria-hidden="true"><rect x="0.8" y="2.5" width="10.4" height="7" rx="0.8" fill="currentColor"/><path d="M1 3 L6 6.8 L11 3" fill="none" stroke="#e96838" stroke-width="1"/></svg>
          <span>d@trvadvisory.example</span>
        </div>
        <div class="contact-line">
          <svg viewBox="0 0 12 12" aria-hidden="true"><circle cx="6" cy="6" r="5" fill="none" stroke="currentColor" stroke-width="1.2"/><ellipse cx="6" cy="6" rx="2" ry="5" fill="none" stroke="currentColor" stroke-width="1"/><path d="M1 6 H11" stroke="currentColor" stroke-width="1"/></svg>
          <span>www.trvadvisory.example</span>
        </div>
      </div>
    </div>
  </section>

  <section class="card card--back" aria-label="Business card back">
    <span class="brand-name">TR Advisory</span>
  </section>
</main>
</body>
</html>
```